DL size Flyer

Design for DL Flyer double sided. One side for blocked drains and pipe relining.
Other side for general plumbing. eg leaking taps, leaking toilets, burst pipes, cctv inspections, gas installations, blocked drains.
Your local plumbing experts.
Relining pictures similar to what we need designed.

Phone number is 0487 312 564 ( on both sides)
Logo for payment methods: cash, quon, cheque. ( on both sides)

Plumbing

```html
<!DOCTYPE html>
<html lang="en">
<head>
<meta charset="utf-8">
<title>Ridgeway Plumbing &amp; Drainage – DL Flyer</title>
<link rel="stylesheet" href="https://fonts.googleapis.com/css2?family=Cabin:ital,wght@0,500;0,700;1,500&family=Oswald:wght@500&family=Exo+2:wght@600&display=swap">
<style>
  :root{
    --bg:#d9d9dd;
    --white:#ffffff;
    --teal:#3fc2a8;
    --teal-dark:#2aa58f;
    --red:#f2201f;
    --blue:#1a8fd0;
    --green:#8ccf0a;
    --ink:#1c1c1c;
    --heading-blue:#1d8fd2;
  }
  *{box-sizing:border-box;margin:0;padding:0}
  html,body{width:1200px;height:1200px;overflow:hidden}
  body{background:var(--bg);font-family:"Cabin",sans-serif;position:relative}
  .flyer{position:absolute;top:120px;width:440px;height:960px;background:var(--white);overflow:hidden}
  .flyer--relining{left:140px}
  .flyer--general{left:620px}

  .brand{position:absolute;top:34px;left:0;width:100%;text-align:center;color:var(--red);font-weight:700;line-height:1.05}
  .brand__name{font-size:34px;letter-spacing:3px;text-transform:uppercase}
  .brand__sub{font-size:15px;letter-spacing:4px;text-transform:uppercase}

  .wave{position:absolute;left:0;width:440px;display:block}

  .hero{position:absolute;top:122px;left:0;width:440px;height:402px;
    background:linear-gradient(180deg,#050505 0%,#0f1a08 35%,#2f6a17 55%,#9a6a2a 72%,#3a3a3a 100%)}
  .hero__headline{position:absolute;top:42px;left:48px;color:var(--white);font-weight:700;font-size:26px;line-height:31px;text-transform:uppercase}
  .guarantee-seal{position:absolute;left:284px;top:90px;width:112px;height:112px;border-radius:50%;background:#8fd12b;border:4px solid #e8f7d2}

  .photo-grid{position:absolute;top:312px;left:0;width:440px;height:212px;
    background:linear-gradient(135deg,#e8e9eb 0%,#b9bcc1 40%,#f3f3f4 60%,#9ea2a8 100%)}

  .intro{position:absolute;text-align:center;font-weight:700;color:var(--ink)}
  .flyer--relining .intro{top:540px;left:52px;width:336px;font-size:13.5px;line-height:17.5px}
  .flyer--general .intro{top:544px;left:44px;width:352px;font-size:12px;line-height:15.6px}

  .benefits{position:absolute;top:632px;left:0;width:440px;height:86px;background:var(--green)}
  .benefits__list{position:absolute;left:190px;top:4px;list-style:none;color:var(--white);font-weight:700;font-size:20px;line-height:26.5px;text-transform:uppercase}
  .no-dig-seal{position:absolute;left:62px;top:622px;width:108px;height:108px;border-radius:50%;background:#7a1d1d;border:6px solid #f2b53a;z-index:3}

  .services{position:absolute;top:634px;left:0;width:440px;height:84px;background:var(--teal);
    font-family:"Oswald",sans-serif;font-size:19px;color:var(--ink);text-align:center;line-height:24px;padding-top:17px;text-transform:uppercase;letter-spacing:-.2px}

  .contact{position:absolute;top:718px;left:0;width:440px;height:118px;background:var(--red);color:var(--white)}
  .contact__phone{position:absolute;top:20px;left:0;width:100%;text-align:center;font-family:"Exo 2",sans-serif;font-weight:600;font-size:30px;letter-spacing:1px}
  .contact__phone svg{vertical-align:-2px;margin-right:8px}
  .contact__email{position:absolute;top:60px;left:0;width:100%;text-align:center;font-size:16px}
  .contact__email svg{vertical-align:-1px;margin-right:10px}
  .contact__social{position:absolute;top:85px;left:0;width:100%;display:flex;justify-content:center;gap:22px;font-size:13.5px}
  .contact__social span{display:flex;align-items:center;gap:7px}
  .contact__social i{display:inline-block;width:11px;height:11px;background:var(--white);border-radius:2px}

  .payments{position:absolute;top:836px;left:0;width:440px;height:124px;background:var(--blue)}
  .payments__list{position:absolute;top:30px;left:0;width:100%;display:flex;justify-content:center;gap:6px;list-style:none}
  .payments__list li{width:50px;height:47px;border-radius:7px;background:var(--white);color:var(--blue);font-weight:700;font-size:8.5px;letter-spacing:0;display:flex;align-items:center;justify-content:center;text-transform:uppercase;white-space:nowrap}

  .promise{position:absolute;top:176px;left:50px;color:var(--heading-blue);font-weight:700;font-size:24.5px;line-height:31px;text-transform:uppercase}
  .tagline{position:absolute;top:254px;left:50px;font-style:italic;font-weight:500;font-size:22px;color:var(--ink)}
</style>
</head>
<body>

<section class="flyer flyer--relining">
  <div class="brand"><div class="brand__name">Ridgeway</div><div class="brand__sub">Plumbing &amp; Drainage</div></div>
  <svg class="wave" style="top:106px" height="22" viewBox="0 0 440 22"><path d="M0 8 Q220 -4 440 8 L440 22 Q220 10 0 22Z" fill="var(--teal)"/></svg>
  <div class="hero" role="img" aria-label="Illustration of an old buried clay pipe broken by tree roots with a new teal liner inserted inside, grass above">
    <h1 class="hero__headline">Reline your<br>pipes to provide<br>a permanent<br>solution</h1>
    <div class="guarantee-seal" role="img" aria-label="Guarantee seal"></div>
  </div>
  <svg class="wave" style="top:512px" height="24" viewBox="0 0 440 24"><path d="M0 14 Q220 -2 440 14 L440 24 L0 24Z" fill="var(--white)"/><path d="M0 10 Q220 -6 440 10 L440 16 Q220 0 0 16Z" fill="var(--teal)"/></svg>
  <p class="intro">Using our state-of-the-art gear, we insert an inner lining into the affected pipe, kind of like key hole surgery. This lining then becomes hard and creates another pipe inside the damaged one.</p>
  <div class="benefits">
    <ul class="benefits__list"><li>It's clean</li><li>It's efficient</li><li>It's cost effective</li></ul>
  </div>
  <div class="no-dig-seal" role="img" aria-label="No dig pipe renewal seal"></div>
  <div class="contact">
    <div class="contact__phone"><svg width="22" height="20" viewBox="0 0 22 20"><path d="M1 6 Q11 -2 21 6 L18 9 L15 6 L7 6 L4 9Z M5 10 L17 10 L20 19 L2 19Z" fill="#fff"/></svg>0487 312 564</div>
    <div class="contact__email"><svg width="16" height="11" viewBox="0 0 16 11"><rect width="16" height="11" fill="#fff"/><path d="M0 0 L8 6 L16 0" stroke="var(--red)" stroke-width="1.5" fill="none"/></svg>info@ridgewayplumbing.example</div>
    <div class="contact__social"><span><i></i>Yourname</span><span><i></i>Yourname</span></div>
  </div>
  <svg class="wave" style="top:826px" height="22" viewBox="0 0 440 22"><path d="M0 4 Q220 -6 440 4 L440 22 L0 22Z" fill="var(--blue)"/><path d="M0 4 Q220 -6 440 4 L440 10 Q220 0 0 10Z" fill="var(--teal-dark)"/></svg>
  <div class="payments"><ul class="payments__list"><li>Cash</li><li>Cheque</li><li>quon</li><li>Tallypay</li></ul></div>
</section>

<section class="flyer flyer--general">
  <div class="brand"><div class="brand__name">Ridgeway</div><div class="brand__sub">Plumbing &amp; Drainage</div></div>
  <svg class="wave" style="top:106px" height="22" viewBox="0 0 440 22"><path d="M0 8 Q220 -4 440 8 L440 16 Q220 4 0 16Z" fill="var(--teal)"/></svg>
  <h1 class="promise">Professional plumbing<br>friendly services!</h1>
  <p class="tagline">Your local plumbing experts!</p>
  <div class="photo-grid" role="img" aria-label="Grid of eight photos of plumbing work: sink pipes, a plumber under a basin, chrome taps, a wrench and shower head"></div>
  <svg class="wave" style="top:512px" height="24" viewBox="0 0 440 24"><path d="M0 14 Q220 -2 440 14 L440 24 L0 24Z" fill="var(--white)"/><path d="M0 10 Q220 -6 440 10 L440 16 Q220 0 0 16Z" fill="var(--teal)"/></svg>
  <p class="intro">We are experts in fixing all major plumbing problems, from water heater repair, faucets, pipes and toilets. We also handles, tub and shower installation and fixtures, faucet repair and replacement, sink installation, repair, drain cleaning, toilet repair and replacement and well systems.</p>
  <div class="services">Leaking taps | Leaking toilets | Burst pipes<br>CCTV inspections | Gas installations | Blocked drains</div>
  <div class="contact">
    <div class="contact__phone"><svg width="22" height="20" viewBox="0 0 22 20"><path d="M1 6 Q11 -2 21 6 L18 9 L15 6 L7 6 L4 9Z M5 10 L17 10 L20 19 L2 19Z" fill="#fff"/></svg>0487 312 564</div>
    <div class="contact__email"><svg width="16" height="11" viewBox="0 0 16 11"><rect width="16" height="11" fill="#fff"/><path d="M0 0 L8 6 L16 0" stroke="var(--red)" stroke-width="1.5" fill="none"/></svg>info@ridgewayplumbing.example</div>
    <div class="contact__social"><span><i></i>Yourname</span><span><i></i>Yourname</span></div>
  </div>
  <svg class="wave" style="top:826px" height="22" viewBox="0 0 440 22"><path d="M0 4 Q220 -6 440 4 L440 22 L0 22Z" fill="var(--blue)"/><path d="M0 4 Q220 -6 440 4 L440 10 Q220 0 0 10Z" fill="var(--teal-dark)"/></svg>
  <div class="payments"><ul class="payments__list"><li>Cash</li><li>Cheque</li><li>quon</li><li>Tallypay</li></ul></div>
</section>

</body>
</html>
```